Commercial Rooftop Solar business needs a website

We need a website with fantastic appeal for a new company based in Melbourne called Brightvale Energy. We design and install solar energy systems for commercial applications across Australia. Our market is to focus on small to medium businesses looking for solar solutions, but we will also provide our service for residential customers. We would like a beautiful 'front page' feel to our home page, using photographs of solar PV systems and/or natural imagery. Our logo uses the colours orange and black, which could easily be echoed in photographic imagery of sunset and sunrise, for example. The design should communicate quiet confidence and professionalism to a corporate marketplace.

NEW POINTS FOR BRIEF: This design also needs to be flexible to allow for additional future content, including a Support page with sub pages, FAQ's, and a Blog.

As part of this design project, we will require the coding for the website to be completed by the designer.

We have seen some websites, which we like the look and feel of: these are listed below.

keenroofpower.com.au:

• Beautiful images underlaying brief text selling points.
• Simple ‘front cover’ style home page with elegant drop-down menu, stylish simple font style.
• Home page invites exploration through the menu links, rather than trying to provide all the information up front.
• Company logo and name in the top left hand corner, contact details accessible at top right hand, seems consistent in most sites.

tolvaenergy.com.au

brinkeltpower.com:
• Same element as the others is the front-page style home page with beautiful images underlying text.

We have a webpage that we started uploading content to. You can use some of the content there in your designs: www.brightvaleenergy.com.au

Technical Specifications:
PAGES:

Home

About Us

Solutions - Commercial
- Residential

Products - Solar Panels - Morvo Falcon, Morvo CELT, Morvo KT
- Solar Inverters - Valtrex, SunPivot
- Monitoring systems - Lumen Metrics
- Batteries - QD

- Datasheets have been provided for reference but if it's too much work, you can use generic text and we will provide content later.

Contact Us

FUTURE PAGES (Please consider in structure, where links could be placed):

Support

FAQ's

Blog.

We could provide some content for the Support page soon, but the Blog and FAQ's are future pages which we don't want highlighted in the design as we don't yet have content.

Phone: 1800 7 VOLTA
Email: sales@brightvaleenergy.com.au

Currently, I do not have images and text available. Please
use placeholders in the meantime. The final text and images will be uploaded for the winner once a winning design has been selected.

Target Market(s)

Primary focus is on small to medium sized business owners. Those owners will have a house which may be suitable for solar so we want to cater to residential deeper in the website.

Industry/Entity Type

Solar Energy

Coding

Coded - Design and coding required

Number of Pages Required

5+ page

Colors
f78f20
0255a3

Requirements
Must have
• Logo as per attachments.
Nice to have
• Logo can have alternate colours Eg. White on Orange or Black etc. provided colour correct logo is shown somewhere eg. footer or contact page.
• In the active site, I'd like to have:
• Very slowly zooming images - barely perceptible.
• Title text that rolls into place
• Subtle movements
• See https://paylarkfinance.com.au/ for example

```html
<!DOCTYPE html>
<html lang="en">
<head>
<meta charset="utf-8">
<title>Brightvale Energy – Commercial</title>
<link href="https://fonts.googleapis.com/css2?family=Raleway:wght@400;500;600;700&family=Open+Sans:wght@400;600&display=swap" rel="stylesheet">
<style>
:root{
  --orange:#f78f20;
  --orange-deep:#e2541c;
  --red:#d8361f;
  --ink:#2b2b2b;
  --body:#555;
  --white:#fff;
  --footer:#1d1d1d;
  --footer-bar:#121212;
  --muted:#9a9a9a;
  --line:#cfcfcf;
}
*{box-sizing:border-box;margin:0;padding:0}
html,body{width:711px;height:1200px;overflow:hidden;background:#fff}
body{font-family:'Open Sans',Arial,sans-serif;color:var(--body);position:relative}

/* hero */
.hero{position:absolute;left:0;top:0;width:711px;height:232px;overflow:hidden}
.hero-photo{position:absolute;inset:0;background:linear-gradient(180deg,#7c8ea0 0%,#9aa7b1 30%,#8c6a55 55%,#6e4a38 75%,#5a4a40 100%)}
.hero-shade{position:absolute;inset:0;background:linear-gradient(180deg,rgba(0,0,0,.55) 0,rgba(0,0,0,.15) 30%,rgba(0,0,0,.25) 100%)}
.topbar{position:absolute;left:0;top:0;width:711px;height:54px;background:rgba(15,15,15,.72);display:flex;align-items:center;padding:0 22px}
.brand{display:flex;align-items:center;gap:7px;font-family:'Raleway',sans-serif;font-weight:700;color:var(--white);font-size:13px;letter-spacing:.5px}
.brand-mark{width:11px;height:11px;background:var(--orange)}
.nav{display:flex;gap:13px;margin-left:auto;margin-top:16px;font-family:'Raleway',sans-serif;font-size:8.5px;font-weight:700;letter-spacing:.5px;color:var(--white)}
.nav .active{color:var(--orange)}
.contact-top{position:absolute;right:22px;top:8px;display:flex;align-items:center;gap:8px;font-family:'Raleway',sans-serif;font-size:9px;font-weight:700;color:var(--white)}
.btn-quote{background:var(--orange);color:var(--white);padding:3px 9px;font-size:8px;letter-spacing:.5px}
.hero-title{position:absolute;top:153px;width:100%;text-align:center;font-family:'Raleway',sans-serif;font-weight:600;font-size:21px;letter-spacing:3px;color:var(--white)}

/* section headings */
.section-heading{display:flex;align-items:center;justify-content:center;gap:14px;font-family:'Raleway',sans-serif;font-weight:500;font-size:22px;letter-spacing:3px;color:var(--ink)}
.section-heading::before,.section-heading::after{content:"";width:150px;height:1px;background:var(--ink)}

/* commercial */
.commercial{position:absolute;top:232px;left:0;width:711px;height:302px;padding:36px 40px 0}
.commercial .section-heading{margin-bottom:18px}
.copy h3{font-size:10.5px;font-weight:400;color:var(--orange-deep);margin:8px 0 3px}
.copy h3.lead{font-size:11.5px}
.copy p{font-size:8px;line-height:1.5;color:var(--body)}

/* proposal */
.proposal{position:absolute;top:534px;left:0;width:711px;height:392px;overflow:hidden}
.proposal-bg{position:absolute;inset:0;background:linear-gradient(160deg,#f7f7f7 0%,#e9eaec 45%,#dfe1e4 70%,#f3f3f3 100%)}
.proposal .section-heading{position:absolute;top:30px;width:100%}
.proposal .section-heading::before,.proposal .section-heading::after{width:170px}
.diagram{position:absolute;left:0;top:70px}
.btn-proposal{position:absolute;left:50%;top:340px;transform:translateX(-50%);background:var(--red);color:var(--white);font-family:'Raleway',sans-serif;font-weight:700;font-size:8.5px;letter-spacing:1px;padding:8px 16px;border-radius:2px}

/* footer */
.footer{position:absolute;top:926px;left:0;width:711px;height:254px;background:var(--footer);padding:26px 40px 0;display:flex;gap:34px;color:var(--muted)}
.footer h4{font-family:'Raleway',sans-serif;font-size:10px;letter-spacing:1px;color:var(--white);font-weight:600;padding-bottom:6px;margin-bottom:10px;border-bottom:1px solid #444;position:relative}
.footer h4::after{content:"";position:absolute;left:0;bottom:-1px;width:30px;height:1px;background:var(--orange)}
.links{width:110px}
.links li{list-style:none;font-size:8.5px;line-height:2.05}
.links li::before{content:"› ";color:var(--orange)}
.inquiry{width:150px}
.field{background:#fff;height:14px;margin-bottom:5px;font-size:7px;color:#999;padding:2px 4px}
.field.msg{height:42px}
.btn-submit{display:inline-block;background:var(--orange-deep);color:#fff;font-size:7px;padding:3px 8px}
.details{width:160px;font-size:8px}
.details .row{display:flex;gap:6px;margin-bottom:8px;line-height:1.4}
.details svg{flex:none;margin-top:1px}
.details .name{color:var(--white);font-weight:600}
.footer-brand{margin-left:auto;text-align:center;padding-top:42px}
.footer-brand .brand{font-size:15px}
.footer-brand .brand-mark{width:13px;height:13px}
.abn{font-size:7px;margin-top:10px}
.copyright{position:absolute;top:1180px;left:0;width:711px;height:20px;background:var(--footer-bar);color:#777;font-size:7px;text-align:center;line-height:20px}
</style>
</head>
<body>

<header class="hero">
  <div class="hero-photo" role="img" aria-label="Photograph of a long brick commercial building with a sawtooth roof under a clear sky"></div>
  <div class="hero-shade"></div>
  <div class="topbar">
    <div class="brand"><span class="brand-mark"></span>Brightvale Energy</div>
    <nav class="nav">
      <span>HOME</span><span>ABOUT US</span><span class="active">COMMERCIAL</span><span>RESIDENTIAL</span><span>PRODUCTS</span><span>CONTACT</span>
    </nav>
    <div class="contact-top">
      <svg width="10" height="10" viewBox="0 0 10 10"><circle cx="5" cy="5" r="5" fill="#f78f20"/><path d="M3 2.6l1 .1.4 1.2-.6.5a4 4 0 0 0 1.8 1.8l.5-.6 1.2.4.1 1C6.6 7.9 2.1 6.5 3 2.6z" fill="#fff"/></svg>
      <span>1800 7 VOLTA</span>
      <span class="btn-quote">FREE QUOTE</span>
    </div>
  </div>
  <h1 class="hero-title">POWERING AUSTRALIAN BUSINESS</h1>
</header>

<section class="commercial">
  <h2 class="section-heading">Commercial</h2>
  <div class="copy">
    <h3 class="lead">Brightvale Energy specialises in energy solutions for small to medium businesses.</h3>
    <p>In a sunburnt country, harnessing the immense power of the sun for the energy requirements of your business is the most practical solution to sustain your business for the long term. This is energy that never runs out, and a way you can reduce your operating costs and protect your business from ever increasing electricity prices.</p>
    <h3>Business Case: No-Cost Solar</h3>
    <p>There are incredibly sound business cases to install solar for your business. With the current Government incentives, provided up front rebates based on Small-scale Technology Certificates (STCs), solar electricity systems can be bought or leased cost effectively, and even potentially provide income through production and export of power to the grid. The result is no-cost solar, the cost being completely off-set by incentives and savings in electricity costs. We offer finance to so can provide your solar energy solution promptly and cost effectively so you can get started right away.</p>
    <h3>Sustainability: Our Environment Matters.</h3>
    <p>Protecting our planet protects all of us: our communities, our health and our future. Using sustainable energy ensures the longevity of our businesses too. Switching to solar power is an investment in the future health of every part of our community life and society, including the running of a healthy business.</p>
    <h3>Free Proposals</h3>
    <p>As part of our service we welcome the opportunity to provide a FREE fully customised proposal that considers your electricity consumption profile, your current and future electricity tariffs plus a full assessment of your facilities suitability for commercial solar power.</p>
  </div>
</section>

<section class="proposal">
  <div class="proposal-bg" role="img" aria-label="Faded photograph of rows of solar panels on a rooftop"></div>
  <h2 class="section-heading">Our Free Proposal</h2>
  <svg class="diagram" width="711" height="260" viewBox="0 0 711 260" font-family="Open Sans, Arial, sans-serif" font-size="10" fill="#444">
    <defs>
      <radialGradient id="dot" cx="40%" cy="35%" r="70%">
        <stop offset="0" stop-color="#ffa23c"/><stop offset="1" stop-color="#e4531b"/>
      </radialGradient>
      <radialGradient id="core" cx="40%" cy="35%" r="70%">
        <stop offset="0" stop-color="#f0552c"/><stop offset="1" stop-color="#b8221a"/>
      </radialGradient>
    </defs>
    <ellipse cx="355" cy="130" rx="112" ry="100" fill="none" stroke="#c8c8c8" stroke-width="1.2"/>
    <circle cx="355" cy="130" r="58" fill="#fff" opacity=".7"/>
    <circle cx="355" cy="130" r="50" fill="url(#core)"/>

    <g stroke="#fff" stroke-width="2.5">
      <circle cx="258" cy="55" r="26" fill="url(#dot)"/>
      <circle cx="452" cy="55" r="26" fill="url(#dot)"/>
      <circle cx="240" cy="133" r="26" fill="url(#dot)"/>
      <circle cx="470" cy="133" r="26" fill="url(#dot)"/>
      <circle cx="258" cy="210" r="26" fill="url(#dot)"/>
      <circle cx="452" cy="210" r="26" fill="url(#dot)"/>
    </g>

    <g fill="none" stroke="#fff" stroke-width="1.6" stroke-linecap="round" stroke-linejoin="round">
      <rect x="250" y="44" width="16" height="21" rx="1.5"/><path d="M254 51h8M254 56h8M254 61h5"/>
      <rect x="442" y="46" width="20" height="17"/><path d="M448.7 46v17M455.3 46v17M442 54.5h20"/>
      <circle cx="240" cy="133" r="10"/><path d="M243 128.5c-1-1-5-1-5.5 1s5 1.5 5 4-4.5 2.5-6 1M240 125.5v15"/>
      <rect x="461" y="122" width="18" height="21" rx="1.5"/><path d="M465 129l1.5 1.5 3-3M465 136l1.5 1.5 3-3M472 129h4M472 136h4"/>
      <circle cx="258" cy="210" r="5"/><path d="M258 199v3M258 218v3M247 210h3M266 210h3M250 202l2 2M264 216l2 2M250 218l2-2M264 204l2-2"/>
      <rect x="442" y="201" width="20" height="18" rx="1.5"/><path d="M442 207h20M447 198v5M457 198v5"/>
    </g>

    <g text-anchor="end">
      <text x="222" y="52">Equipment</text><text x="222" y="65">Specifications</text>
      <text x="204" y="137">Investment Return</text>
      <text x="222" y="214">System Yield</text>
    </g>
    <g text-anchor="start">
      <text x="489" y="59">Module Layout</text>
      <text x="506" y="137">Scope of Works</text>
      <text x="489" y="207">Estimated Monthly &amp;</text><text x="489" y="220">Yearly Savings</text>
    </g>
  </svg>
  <div class="btn-proposal">REQUEST A FREE PROPOSAL</div>
</section>

<footer class="footer">
  <div class="links">
    <h4>Quick Links</h4>
    <ul>
      <li>Home</li><li>About Us</li><li>Commercial</li><li>Residential</li><li>Products</li><li>Contact</li>
    </ul>
  </div>
  <div class="inquiry">
    <h4>Quick Inquiry</h4>
    <div class="field">Name</div>
    <div class="field">Email</div>
    <div class="field msg">Message</div>
    <span class="btn-submit">SUBMIT</span>
  </div>
  <div class="details">
    <h4>Contact Details</h4>
    <div class="row"><svg width="9" height="9" viewBox="0 0 10 10"><path d="M2 1l2 .2.7 2-1 .8a5 5 0 0 0 2.3 2.3l.8-1 2 .7.2 2C5 9 1 5 2 1z" fill="#f78f20"/></svg><span>1800 7 VOLTA</span></div>
    <div class="row"><svg width="9" height="9" viewBox="0 0 10 10"><rect x="1" y="2" width="8" height="6" fill="none" stroke="#f78f20" stroke-width="1.2"/><path d="M1 2l4 3.5L9 2" fill="none" stroke="#f78f20" stroke-width="1.2"/></svg><span>sales@brightvaleenergy.com.au</span></div>
    <div class="row"><svg width="9" height="9" viewBox="0 0 10 10"><circle cx="5" cy="5" r="4" fill="none" stroke="#f78f20" stroke-width="1.2"/><path d="M1 5h8M5 1c-2 2.5-2 5.5 0 8M5 1c2 2.5 2 5.5 0 8" fill="none" stroke="#f78f20" stroke-width=".9"/></svg><span>www.brightvaleenergy.com.au</span></div>
    <div class="row"><svg width="9" height="9" viewBox="0 0 10 10"><path d="M5 9.5S1.5 6 1.5 4a3.5 3.5 0 0 1 7 0c0 2-3.5 5.5-3.5 5.5z" fill="#f78f20"/><circle cx="5" cy="4" r="1.2" fill="#1d1d1d"/></svg><span><span class="name">BRIGHTVALE ENERGY</span><br>Carrow Park, Victoria</span></div>
  </div>
  <div class="footer-brand">
    <div class="brand"><span class="brand-mark"></span>Brightvale Energy</div>
    <div class="abn">ABN 00 000 000 000</div>
  </div>
</footer>
<div class="copyright">Copyright © 2017 Brightvale Energy. All Rights Reserved.</div>

</body>
</html>
```